Landing page design for my current website

I need a landing page designed for my Wordpress website. My website is Plumvarick.com, and I need a page that will serve as a landing page for online ads I run. Please follow the color scheme of the current website

This web page will be targeted towards real estate owners who are looking for a property manager. Above the fold needs to have a CTA form headlined with "As a Rental Property Owner, I Want More Protection, Less Stress, and Drama-Free Living"

A few highlights that can be listed beyond the CTA and fold

- Comprehensive Property Management
Full-service management covering tenant placement, leasing, maintenance, and inspections.

Maximized Rental Income
Proven strategies to optimize rental rates and minimize vacancies, ensuring higher ROI.

Stress-Free Management
We handle all tenant interactions, maintenance requests, and property issues, so you don't have to.

Experienced Team
Over a decade of experience in managing single-family homes, small multifamily units, and apartment complexes.

Advanced Technology
Utilize cutting-edge property management software for efficient communication, rent collection, and maintenance tracking.

Tenant Screening and Placement
Thorough background checks and tenant screening processes to ensure reliable and responsible tenants.

Regular Property Inspections
Routine inspections to maintain property condition and address issues before they become costly problems.

Legal Compliance
Expertise in local and federal rental laws to keep your properties compliant and avoid legal hassles.

Transparent Reporting
Detailed monthly reports and financial statements to keep you informed about your property's performance.

Personalized Service
Tailored management plans to meet the unique needs of your properties and investment goals.
Effective Tenant Conflict Resolution
Skilled in handling challenging tenant situations, ensuring conflicts are resolved quickly and professionally to maintain a peaceful living environment and protect your investment.

```html
<!DOCTYPE html>
<html lang="en">
<head>
<meta charset="utf-8">
<title>Plumvarick Realty – Property Management</title>
<link href="https://fonts.googleapis.com/css2?family=Rajdhani:wght@600;700&family=Montserrat:wght@600;700&family=Lato:wght@400&display=swap" rel="stylesheet">
<style>
:root{
  --navy:#154a86;
  --ink:#1a1a1a;
  --text:#333;
  --disc:#e6eaef;
  --ring:#2b2b2b;
  --footer:#000;
  --white:#fff;
}
*{box-sizing:border-box;margin:0;padding:0}
html,body{width:1200px;height:2493px;overflow:hidden}
body{position:relative;background:var(--white);font-family:"Lato",sans-serif;color:var(--text)}
.site-header{position:absolute;top:0;left:0;width:1200px;height:86px;background:var(--white)}
.brand{position:absolute;left:97px;top:22px;display:flex;align-items:center;gap:12px}
.brand-dot{width:42px;height:42px;border-radius:50%;background:var(--navy)}
.brand-name{font-family:"Rajdhani",sans-serif;font-weight:700;font-size:27px;color:var(--navy);letter-spacing:.5px}
.main-nav{position:absolute;left:581px;top:34px;display:flex;gap:24px;font-family:"Rajdhani",sans-serif;font-weight:700;font-size:15px;color:var(--ink)}
.main-nav .active{color:var(--navy);border-bottom:2px solid var(--navy);padding-bottom:2px}
.btn{display:inline-flex;align-items:center;gap:8px;background:var(--navy);color:var(--white);font-family:"Rajdhani",sans-serif;font-weight:700;font-size:18px;border-radius:3px;box-shadow:0 2px 4px rgba(0,0,0,.3)}
.header-cta{position:absolute;left:962px;top:20px;width:140px;height:47px;justify-content:center}
.hero{position:absolute;top:86px;left:0;width:1200px;height:635px;background:linear-gradient(100deg,#2d3440 0%,#6b6e72 30%,#8d8f90 50%,#50555c 75%,#7b7f82 100%)}
.lead-form{position:absolute;left:625px;top:184px;width:476px;height:439px;background:var(--white);padding:30px 32px}
.lead-form h1{font-family:"Montserrat",sans-serif;font-weight:600;font-size:21px;line-height:31px;color:#2a2a2a}
.field{position:relative;margin-top:24px;height:49px;border:1px solid #ccc;padding:0 20px;display:flex;align-items:center;justify-content:space-between;font-size:15px;color:#444}
.field + .field{margin-top:20px}
.form-submit{margin-top:26px;width:141px;height:47px;justify-content:center}
.highlights-title{position:absolute;top:805px;width:1200px;text-align:center;font-family:"Rajdhani",sans-serif;font-weight:700;font-size:39px;color:var(--ink)}
.title-rule{position:absolute;top:863px;left:580px;width:40px;height:3px;background:var(--ink)}
.feature{position:absolute;width:520px;height:200px}
.feature-icon{position:absolute;left:0;top:0}
.feature-bar{position:absolute;top:18px;width:3px;height:90px;background:var(--navy)}
.feature-body{position:absolute;top:12px}
.feature-body h2{font-family:"Rajdhani",sans-serif;font-weight:700;font-size:23px;line-height:31px;color:var(--navy)}
.feature-body p{font-size:16px;line-height:31px;margin-top:4px;color:#333}
.col-l{left:97px}.col-l .feature-bar{left:178px}.col-l .feature-body{left:203px;width:300px}
.col-r{left:620px}.col-r .feature-bar{left:173px}.col-r .feature-body{left:210px;width:290px}
.site-footer{position:absolute;top:2067px;left:0;width:1200px;height:426px;background:var(--footer);color:var(--white)}
.foot-col{position:absolute;top:58px}
.foot-col h3{font-family:"Montserrat",sans-serif;font-weight:700;font-size:21px;margin-bottom:10px}
.foot-list{list-style:none;font-size:16px}
.foot-list li{height:31px;display:flex;align-items:center;gap:10px}
.contact-row{display:flex;align-items:center;gap:12px;height:60px;font-size:16px}
.contact-icon{width:37px;height:37px;border-radius:50%;background:var(--white);display:flex;align-items:center;justify-content:center}
.news-text{font-size:16px;line-height:31px;margin-top:16px}
.news-email{margin-top:8px;width:270px;border-bottom:2px solid var(--white);padding:0 0 8px 3px;font-size:16px}
.subscribe{margin:30px 0 0 7px;width:146px;height:51px;background:var(--white);color:var(--ink);font-family:"Montserrat",sans-serif;font-weight:600;font-size:18px;display:flex;align-items:center;justify-content:center}
.foot-rule{position:absolute;top:365px;left:98px;width:1003px;height:1px;background:#ccc}
.copyright{position:absolute;top:383px;width:1200px;text-align:center;font-size:16px}
</style>
</head>
<body>
<svg width="0" height="0" style="position:absolute">
  <defs>
    <symbol id="ring" viewBox="0 0 140 140">
      <path d="M118 22 A68 68 0 1 0 118 118" fill="none" stroke="var(--ring)" stroke-width="8"/>
      <path d="M60 5 A66 66 0 0 1 132 40" fill="none" stroke="var(--navy)" stroke-width="8"/>
      <path d="M132 100 A66 66 0 0 1 60 135" fill="none" stroke="var(--navy)" stroke-width="8"/>
      <circle cx="72" cy="70" r="45" fill="var(--disc)"/>
      <path d="M55 75 L72 60 L89 75 M59 72 V88 H85 V72" fill="none" stroke="var(--navy)" stroke-width="2"/>
    </symbol>
    <symbol id="arrow" viewBox="0 0 14 14"><path d="M1 7 H11 M7 2 L12 7 L7 12" fill="none" stroke="currentColor" stroke-width="2.6"/></symbol>
  </defs>
</svg>

<header class="site-header">
  <div class="brand"><span class="brand-dot"></span><span class="brand-name">PLUMVARICK REALTY</span></div>
  <nav class="main-nav"><span class="active">HOME</span><span>RESIDENTS</span><span>INVESTORS</span><span>COMMUNITIES</span></nav>
  <a class="btn header-cta">Contact Us <svg width="14" height="14"><use href="#arrow"/></svg></a>
</header>

<section class="hero" role="img" aria-label="Photo of a person signing a contract beside architectural building models"></section>
<form class="lead-form">
  <h1>As a Rental Property Owner, I Want More Protection, Less Stress, and Drama-Free Living</h1>
  <div class="field">Name <svg width="18" height="18" viewBox="0 0 18 18"><circle cx="9" cy="6" r="4" fill="none" stroke="#333"/><path d="M2 17 Q9 8 16 17Z" fill="none" stroke="#333"/></svg></div>
  <div class="field">Phone <svg width="18" height="18" viewBox="0 0 18 18"><path d="M3 2 L6 2 L8 6 L6 8 Q8 12 11 13 L13 11 L17 13 L16 16 Q8 16 3 2Z" fill="none" stroke="#333"/></svg></div>
  <div class="field">Email <svg width="22" height="16" viewBox="0 0 22 16"><rect x="1" y="1" width="20" height="14" fill="none" stroke="#333" stroke-width="1.4"/><path d="M1 1 L11 9 L21 1 M1 15 L8 7 M21 15 L14 7" fill="none" stroke="#333" stroke-width="1.4"/></svg></div>
  <a class="btn form-submit">Submit <svg width="14" height="14"><use href="#arrow"/></svg></a>
</form>

<h2 class="highlights-title">Our Highlights</h2>
<div class="title-rule"></div>

<article class="feature col-l" style="top:910px"><svg class="feature-icon" width="140" height="140"><use href="#ring"/></svg><span class="feature-bar"></span><div class="feature-body"><h2>Comprehensive Property Management</h2><p>Full-service management covering tenant placement, leasing,</p></div></article>
<article class="feature col-r" style="top:910px"><svg class="feature-icon" width="140" height="140"><use href="#ring"/></svg><span class="feature-bar"></span><div class="feature-body"><h2>Maximized Rental Income</h2><p>Proven strategies to optimize rental rates and minimize vacancies, ensuring higher ROI.</p></div></article>

<article class="feature col-l" style="top:1123px"><svg class="feature-icon" width="140" height="140"><use href="#ring"/></svg><span class="feature-bar"></span><div class="feature-body"><h2>Stress-Free Management</h2><p>We handle all tenant interactions, maintenance requests, and property issues, so you don't have to.</p></div></article>
<article class="feature col-r" style="top:1123px"><svg class="feature-icon" width="140" height="140"><use href="#ring"/></svg><span class="feature-bar"></span><div class="feature-body"><h2>Experienced Team</h2><p>Over a decade of experience in managing single-family homes, small multifamily units, and apartment complexes.</p></div></article>

<article class="feature col-l" style="top:1353px"><svg class="feature-icon" width="140" height="140"><use href="#ring"/></svg><span class="feature-bar"></span><div class="feature-body"><h2>Advanced Technology</h2><p>Utilize cutting-edge property management software for efficient communication, rent collection, and maintenance tracking.</p></div></article>
<article class="feature col-r" style="top:1353px"><svg class="feature-icon" width="140" height="140"><use href="#ring"/></svg><span class="feature-bar"></span><div class="feature-body" style="top:6px"><h2>Tenant Screening and Placement</h2><p>Thorough background checks and tenant screening processes to ensure reliable and responsible tenants.</p></div></article>

<article class="feature col-l" style="top:1578px"><svg class="feature-icon" width="140" height="140"><use href="#ring"/></svg><span class="feature-bar"></span><div class="feature-body" style="width:320px"><h2>Regular Property Inspections</h2><p>Routine inspections to maintain property condition and address issues before they become costly problems.</p></div></article>
<article class="feature col-r" style="top:1578px"><svg class="feature-icon" width="140" height="140"><use href="#ring"/></svg><span class="feature-bar"></span><div class="feature-body" style="top:6px"><h2>Legal Compliance</h2><p>Expertise in local and federal rental laws to keep your properties compliant and avoid legal hassles.</p></div></article>

<article class="feature col-l" style="top:1803px"><svg class="feature-icon" width="140" height="140"><use href="#ring"/></svg><span class="feature-bar"></span><div class="feature-body"><h2>Transparent Reporting</h2><p>Detailed monthly reports and financial statements to keep you informed about your property's performance.</p></div></article>
<article class="feature col-r" style="top:1803px"><svg class="feature-icon" width="140" height="140"><use href="#ring"/></svg><span class="feature-bar"></span><div class="feature-body" style="top:6px"><h2>Personalized Service</h2><p>Tailored management plans to meet the unique needs of your properties and investment goals.</p></div></article>

<footer class="site-footer">
  <div class="foot-col" style="left:97px"><h3>Main Links</h3>
    <ul class="foot-list"><li><svg width="14" height="14" color="#fff"><use href="#arrow"/></svg>Home</li><li><svg width="14" height="14" color="#fff"><use href="#arrow"/></svg>For Investors</li><li><svg width="14" height="14" color="#fff"><use href="#arrow"/></svg>Residents</li><li><svg width="14" height="14" color="#fff"><use href="#arrow"/></svg>Contact</li></ul></div>
  <div class="foot-col" style="left:297px"><h3>Service Areas</h3>
    <ul class="foot-list"><li><svg width="14" height="14" color="#fff"><use href="#arrow"/></svg>Alder Falls</li><li><svg width="14" height="14" color="#fff"><use href="#arrow"/></svg>Cedarmoor</li><li><svg width="14" height="14" color="#fff"><use href="#arrow"/></svg>Hollin Ridge</li><li><svg width="14" height="14" color="#fff"><use href="#arrow"/></svg>Marrow Bend</li></ul></div>
  <div class="foot-col" style="left:508px"><h3>Contact Us</h3>
    <div class="contact-row"><span class="contact-icon"><svg width="14" height="16" viewBox="0 0 14 16"><path d="M7 15 Q1 8 1 6 A6 6 0 0 1 13 6 Q13 8 7 15Z" fill="#000"/><circle cx="7" cy="6" r="2" fill="#fff"/></svg></span>Company Name,United State.</div>
    <div class="contact-row"><span class="contact-icon"><svg width="16" height="12" viewBox="0 0 16 12"><rect width="16" height="12" rx="2" fill="#000"/><path d="M1 2 L8 7 L15 2" fill="none" stroke="#fff" stroke-width="1.4"/></svg></span>hello@Plumvarick.com</div>
    <div class="contact-row"><span class="contact-icon"><svg width="15" height="15" viewBox="0 0 18 18"><path d="M3 2 L6 2 L8 6 L6 8 Q8 12 11 13 L13 11 L17 13 L16 16 Q8 16 3 2Z" fill="#000"/></svg></span>555.014.2290</div></div>
  <div class="foot-col" style="left:828px"><h3>Sign Up To Our Newsletter</h3>
    <p class="news-text">Lorem ipsum dolor sit amet,consectetur adipiscing elit,adipiscing elit.</p>
    <div class="news-email">Email</div>
    <div class="subscribe">Subscribe</div></div>
  <div class="foot-rule"></div>
  <p class="copyright">Copyrights@2024.Company Name.All Rights Reserved</p>
</footer>
</body>
</html>
```